Verdant Medispa Business Card

need a business card for our medispa, attached please see the logo.
our website is https://verdantmedispa-example.com

Sorina Belcourt, MD
Internal Medicine

555-204-7193

Sorina@verdantmedispa-example.com

Www.Verdantmedispa-example.com

738 E Harlow Blvd N, Ste 512, Katy, TX 77981

Target Market(s)

MedSpa, Cosmetics, Esthetics

Industry/Entity Type

MedicalSpa

Contact Information for Business Card

Please see the attached business card which i pulled from the internet. I like the idea back as a logo and front with info.

Font styles to use
Decorative

Requirements
Must have
• Color should be matching with Logo and Website theme, Also I like to have QR code for the website

```html
<!DOCTYPE html>
<html lang="en">
<head>
<meta charset="utf-8">
<title>Verdant Medispa Business Card</title>
<link rel="stylesheet" href="https://fonts.googleapis.com/css2?family=Lora:wght@400;500&display=swap">
<style>
  :root {
    --backdrop: #2d2d2d;
    --card-light: #8d7660;
    --card-dark: #6f5b49;
    --gold: #e0b62a;
    --ink-light: #ffffff;
    --ink-soft: #f3ece4;
    --slot-text: #7a6654;
  }
  * { box-sizing: border-box; margin: 0; padding: 0; }
  html, body { width: 1200px; height: 900px; overflow: hidden; }
  body {
    background: var(--backdrop);
    font-family: "Lora", Georgia, serif;
    position: relative;
  }
  .card {
    position: absolute;
    width: 540px;
    height: 309px;
    border-radius: 22px;
    background: radial-gradient(ellipse at 60% 40%, var(--card-light), var(--card-dark));
    box-shadow: 0 14px 30px rgba(0,0,0,0.45);
    overflow: hidden;
  }
  .card--front { left: 40px; top: 296px; }
  .card--back { left: 620px; top: 296px; }

  .brand-name {
    position: absolute;
    color: var(--gold);
    font-weight: 400;
    line-height: 1.1;
    text-align: center;
  }
  .card--front .brand-name {
    left: 28px; top: 96px; width: 190px;
    font-size: 30px;
  }
  .card--back .brand-name {
    left: 230px; top: 54px; width: 260px;
    font-size: 36px;
  }

  .divider {
    position: absolute;
    left: 236px; top: 60px;
    width: 1px; height: 190px;
    background: var(--ink-soft);
  }

  .contact {
    position: absolute;
    left: 252px; top: 64px;
    color: var(--ink-light);
    font-size: 13.5px;
    line-height: 1.45;
  }
  .contact__name {
    color: var(--gold);
    font-size: 21px;
    font-weight: 500;
    line-height: 1.2;
  }
  .contact__role { margin-bottom: 8px; }
  .contact__address { margin-bottom: 6px; }
  .contact__line {
    display: flex;
    align-items: center;
    gap: 6px;
  }
  .contact__line svg { width: 11px; height: 11px; flex: none; }

  .appointment-slot {
    position: absolute;
    left: 58px; top: 172px;
    width: 330px; height: 42px;
    background: var(--ink-light);
    border-radius: 12px;
    display: flex;
    align-items: center;
    padding: 0 14px;
    gap: 6px;
    color: var(--slot-text);
    font-size: 13px;
  }
  .appointment-slot__dots {
    flex: 1;
    border-bottom: 1px dotted var(--slot-text);
    height: 10px;
  }
  .back-web {
    position: absolute;
    left: 72px; top: 228px;
    color: var(--ink-light);
    font-size: 14px;
    font-weight: 500;
  }
</style>
</head>
<body>
  <section class="card card--front" aria-label="Business card front">
    <div class="brand-name">Verdant Medispa</div>
    <div class="divider"></div>
    <div class="contact">
      <p class="contact__name">Sorina Belcourt, MD</p>
      <p class="contact__role">Internal Medicine</p>
      <p class="contact__address">738 E Harlow Blvd N, Ste 512<br>Katy, TX 77981</p>
      <p class="contact__line">
        <svg viewBox="0 0 12 12" aria-hidden="true"><path fill="var(--gold)" d="M2.4 1l2 2.1-1 1.2c.7 1.5 1.8 2.6 3.3 3.3l1.2-1 2.1 2-1 1.5C5 10 2 7 .9 2z"/></svg>
        555-204-7193
      </p>
      <p class="contact__line">
        <svg viewBox="0 0 12 12" aria-hidden="true"><rect x="0.5" y="2" width="11" height="8" fill="var(--gold)"/><path d="M0.5 2.5L6 6.5l5.5-4" stroke="var(--card-dark)" stroke-width="1" fill="none"/></svg>
        Sorina@verdantmedispa-example.com
      </p>
      <p class="contact__line">
        <svg viewBox="0 0 12 12" aria-hidden="true"><circle cx="6" cy="6" r="5.2" fill="none" stroke="var(--gold)" stroke-width="1.2"/><ellipse cx="6" cy="6" rx="2.2" ry="5.2" fill="none" stroke="var(--gold)" stroke-width="1"/><path d="M1 6h10" stroke="var(--gold)" stroke-width="1"/></svg>
        Www.Verdantmedispa-example.com
      </p>
    </div>
  </section>

  <section class="card card--back" aria-label="Business card back">
    <div class="brand-name">Verdant Medispa</div>
    <div class="appointment-slot">
      <span>Date</span><span class="appointment-slot__dots"></span>
      <span>Time</span><span class="appointment-slot__dots"></span>
    </div>
    <p class="back-web">www.Verdantmedispa-example.com</p>
  </section>
</body>
</html>
```